Modern card design needed for building development company

We are looking for a sharp modern new look for our business cards.
We are a New Zealand based company called TKR Ventures NZ LTD that specialises in subdividing large sections, housing and commercial buildings.
We have attached a photo of the current logo and would like to see it improved somehow as it looks a bit dated.
We are open to any colours.

Target Market(s)

Investors, Property buyers

Industry/Entity Type

Investment

Contact Information for Business Card

TKR VENTURES NZ LTD
www.tkrventuresnz.example.nz

Dorian Fletcher
Phone +64 21 843 209
Email dpfletcher@mailvane.example.nz

Font styles to use
Serif
Sans Serif

Colors
0792cd
33a6d7
85cae6
6b449b
886aae
f04a50
ec1f27
f37122
f68d4d

Requirements
Must have
• Please try and make the logo more modern or if you have a similar one we would like to see it.

```html
<!DOCTYPE html>
<html lang="en">
<head>
<meta charset="utf-8">
<title>TKR Ventures NZ LTD — Business Card</title>
<link rel="stylesheet" href="https://fonts.googleapis.com/css2?family=Montserrat:wght@400;500;700&display=swap">
<style>
  :root {
    --backdrop: #dadada;
    --brand-blue: #0792cd;
    --card-white: #ffffff;
    --ink: #111111;
    --on-blue: #ffffff;
  }
  * { box-sizing: border-box; margin: 0; padding: 0; }
  html, body {
    width: 1200px;
    height: 1200px;
    overflow: hidden;
    background: var(--backdrop);
    font-family: "Montserrat", sans-serif;
  }
  .sheet {
    position: relative;
    width: 1200px;
    height: 1200px;
  }
  .card {
    position: absolute;
    left: 250px;
    width: 700px;
    height: 400px;
  }
  .card--front {
    top: 150px;
    background: var(--card-white);
  }
  .card--back {
    top: 650px;
    background: var(--brand-blue);
  }

  /* Front side */
  .holder-name {
    position: absolute;
    left: 110px;
    top: 150px;
    color: var(--brand-blue);
    font-weight: 700;
    font-size: 21px;
  }
  .contact {
    position: absolute;
    left: 100px;
    top: 300px;
    list-style: none;
    font-size: 16px;
    line-height: 22px;
    color: var(--ink);
  }
  .contact__label {
    color: var(--brand-blue);
    margin-right: 4px;
  }
  .brand-lockup {
    position: absolute;
    right: 45px;
    bottom: 45px;
    display: flex;
    align-items: center;
    gap: 10px;
  }
  .brand-lockup__mark {
    width: 18px;
    height: 18px;
    background: var(--brand-blue);
  }
  .brand-lockup__name {
    font-weight: 700;
    font-size: 19px;
    color: var(--ink);
  }

  /* Back side */
  .back-brand {
    position: absolute;
    left: 0;
    right: 0;
    top: 150px;
    display: flex;
    justify-content: center;
    align-items: center;
    gap: 12px;
  }
  .back-brand__mark {
    width: 22px;
    height: 22px;
    background: var(--on-blue);
  }
  .back-brand__name {
    font-weight: 700;
    font-size: 24px;
    color: var(--on-blue);
  }
  .website {
    position: absolute;
    left: 0;
    right: 0;
    top: 250px;
    text-align: center;
    color: var(--on-blue);
    font-size: 16px;
    font-weight: 500;
  }
</style>
</head>
<body>
  <main class="sheet">
    <section class="card card--front" aria-label="Card front">
      <h1 class="holder-name">Dorian Fletcher</h1>
      <ul class="contact">
        <li><span class="contact__label">P:</span>+64 21 843 209</li>
        <li><span class="contact__label">E:</span>dpfletcher@mailvane.example.nz</li>
      </ul>
      <div class="brand-lockup">
        <span class="brand-lockup__mark"></span>
        <span class="brand-lockup__name">TKR Ventures NZ LTD</span>
      </div>
    </section>

    <section class="card card--back" aria-label="Card back">
      <div class="back-brand">
        <span class="back-brand__mark"></span>
        <span class="back-brand__name">TKR Ventures NZ LTD</span>
      </div>
      <p class="website">www.tkrventuresnz.example.nz</p>
    </section>
  </main>
</body>
</html>
```